Member Dashboard needs a facelift

Our company is in the consumer credit industry. We offer a service, and once a person signs up for that service, they become a "Member". As a member, they can sign into our "Member Dashboard". What we are looking for is a facelift to our current "Member Dashboard" pages.

We are looking for a cleaner, more modern design that incorporates the same functionality of the current pages (tabs and charts). The graphics elements, buttons and top navigation menu need updating as well.

We are looking for only the page design "look and Feel" and some new great ideas graphicly. Not looking for an entire site.

Please note that the grey background shown in the screen shots is full browser width.

Thank you.
Updates

Thank you everyone for your designs.  Please make sure all designs are in by the end of day.  We will be selecting the 1st and 2nd design tomorrow AM.

 

Thank you for your partisapation.

 

Target Market(s)

Adults over the age of 18 who pay rent in housing.

Industry/Entity Type

Industry

Requirements
Must have
• We are looking for a professional modern look that keeps with the current structure of the current member dashboard. The pages are 1152px wide.

```html
<!DOCTYPE html>
<html lang="en">
<head>
<meta charset="utf-8">
<title>Member Dashboard</title>
<link href="https://fonts.googleapis.com/css2?family=Arimo:wght@400;700&display=swap" rel="stylesheet">
<style>
:root{
  --page:#d9e1e1;
  --ink:#222;
  --panel:#1e2321;
  --white:#fff;
  --cyan:#1fc0ea;
  --teal:#236473;
  --slate:#5a696e;
  --soft:#d4f7f5;
  --bright:#0bc0ee;
  --deep:#0a4556;
  --pie-grey:#b8c2c6;
  --pie-teal:#236473;
  --pie-dark:#343f42;
  --pie-blue:#5dbdd4;
  --foot-top:#0e5766;
  --foot-bottom:#03222a;
  --foot-text:#5bbfd4;
}
*{margin:0;padding:0;box-sizing:border-box}
html,body{width:900px;height:1200px;overflow:hidden}
body{background:var(--page);font-family:"Arimo",Arial,sans-serif;color:var(--ink);position:relative}
.abs{position:absolute}
.account-links{left:752px;top:265px;font-size:18px;line-height:24px;list-style:none}
.main-nav{list-style:none}
.main-nav li{position:absolute;top:331px;height:34px;border:3px solid var(--white);color:var(--white);font-size:16px;padding:6px 0 0 16px;background:var(--slate)}
.main-nav li.active{background:var(--teal)}
.sub-tab{height:18px;background:var(--panel);border:2px solid var(--white);color:var(--white);font-size:9px;padding:3px 0 0 8px}
.panel{background:var(--panel);border:3px solid var(--white);border-radius:18px;color:var(--white)}
.panel-title{color:var(--cyan);font-size:21px;font-weight:400}
.lorem{font-size:9px;line-height:11px;margin-top:8px}
.field{color:var(--cyan);font-size:9px}
.edit-btn{left:29px;top:670px;width:78px;height:20px;border-radius:10px;background:linear-gradient(#5a8f9c,#2b5b67);border:1px solid #9bc;color:var(--white);font-size:9px;padding:4px 0 0 24px}
.gauge-label{font-size:9px;color:var(--white);text-align:center;width:150px}
.legend{font-size:9px;display:flex;align-items:center;gap:4px}
.sw{width:10px;height:10px;display:inline-block}
.factor{font-size:15px;display:flex;align-items:center;gap:12px}
.factor .sw{width:16px;height:16px}
.cta{left:533px;top:833px;width:329px;height:78px;border:2px solid #cfe;border-radius:8px;background:linear-gradient(#2f6e7e,#1c4f5b);color:var(--white);font-size:18px;font-weight:700;padding:30px 0 0 13px}
.footer{left:2px;top:957px;width:896px;height:243px;background:linear-gradient(var(--foot-top),var(--foot-bottom) 45%)}
.tip{position:absolute;text-align:center;width:140px}
.tip h3{font-weight:400;font-size:22px;color:var(--white);margin-top:21px}
.tip p{font-size:16px;line-height:19.5px;color:var(--foot-text);margin-top:12px}
.more{position:absolute;top:160px;font-size:13px;color:var(--white)}
</style>
</head>
<body>
<ul class="account-links abs"><li>Contact Support</li><li>Logout</li></ul>

<ul class="main-nav">
  <li class="active" style="left:65px;width:191px">Member Home</li>
  <li style="left:272px;width:187px">Rent Profile</li>
  <li style="left:470px;width:192px">Credit Summary</li>
  <li style="left:674px;width:191px">FAQs</li>
</ul>

<div class="sub-tab abs" style="left:44px;top:403px;width:110px">Member Name</div>
<div class="sub-tab abs" style="left:158px;top:402px;width:112px">Rental Address</div>
<div class="sub-tab abs" style="left:275px;top:402px;width:111px">Member &nbsp;Contact</div>

<section class="panel abs" style="left:16px;top:427px;width:486px;height:281px">
  <h2 class="panel-title abs" style="left:13px;top:13px">Landlord Verification Center</h2>
  <div class="abs" style="left:14px;top:40px;width:450px">
    <p class="lorem">Sed ut perspiciatis unde omnis iste natus error sit voluptatem accusantium doloremque laudantium, totam rem aperiam, eaque ipsa quae ab illo inventore veritatis et quasi architecto beatae vitae dicta sunt explicabo. Nemo enim ipsam voluptatem quia voluptas sit aspernatur aut odit aut fugit, sed quia consequuntur magni dolores eos qui ratione voluptatem sequi nesciunt. Neque porro quisquam est, qui</p>
    <p class="lorem">Sed ut perspiciatis unde omnis iste natus error sit voluptatem accusantium doloremque laudantium, totam rem aperiam, eaque ipsa quae ab illo inventore veritatis et quasi architecto beatae vitae dicta sunt explicabo. Nemo enim ipsam voluptatem quia voluptas sit aspernatur aut odit aut fugit, sed quia consequuntur magni dolores eos qui ratione voluptatem sequi nesciunt. Neque porro quisquam est, qui</p>
  </div>
  <span class="field abs" style="left:14px;top:152px">Landlord Management</span>
  <span class="field abs" style="left:124px;top:152px">Complex/Property Name</span>
  <span class="field abs" style="left:249px;top:152px">Street Address 1</span>
  <span class="field abs" style="left:14px;top:175px">Street Address</span>
  <span class="field abs" style="left:124px;top:175px">City</span>
  <span class="field abs" style="left:249px;top:175px">State</span>
  <span class="field abs" style="left:14px;top:199px">Zip Code</span>
  <span class="field abs" style="left:124px;top:199px">Landlord Phone Number</span>
  <span class="field abs" style="left:249px;top:199px">Landlord Fax Number</span>
  <span class="field abs" style="left:14px;top:222px">Landlord Email</span>
</section>
<div class="sub-tab abs" style="left:387px;top:416px;width:107px;border-bottom:none;padding-left:16px">Landlord Contact</div>
<div class="edit-btn abs">Edit
  <svg class="abs" style="left:44px;top:3px" width="20" height="12" viewBox="0 0 20 12"><path d="M2 9 L14 2 L18 6 L6 11 Z" fill="#fff"/></svg>
</div>

<section class="panel abs" style="left:511px;top:427px;width:377px;height:281px">
  <h2 class="panel-title abs" style="left:15px;top:17px">Member Verifcation Center</h2>
  <div class="abs" style="left:13px;top:43px;width:128px;height:112px;border:2px solid #ccc;border-radius:6px"></div>
</section>

<svg class="abs" style="left:0;top:0" width="900" height="720" aria-hidden="true">
  <defs>
    <g id="dial">
      <path d="M56 56 L0 56 A56 56 0 0 1 28 7.5 Z" fill="var(--soft)"/>
      <path d="M56 56 L28 7.5 A56 56 0 0 1 88.1 10.1 Z" fill="var(--bright)"/>
      <path d="M56 56 L88.1 10.1 A56 56 0 0 1 112 56 Z" fill="var(--deep)"/>
    </g>
  </defs>
  <g transform="translate(533,497)"><use href="#dial"/><polygon points="50,62 97.5,24.7 58,52" fill="#000" stroke="#fff" stroke-width="1.5"/></g>
  <g transform="translate(750,497)"><use href="#dial"/><polygon points="51,58 40,4 61,56" fill="#000" stroke="#fff" stroke-width="1.5"/></g>
  <g transform="translate(533,595)"><use href="#dial"/><polygon points="51,58 40,4 61,56" fill="#000" stroke="#fff" stroke-width="1.5"/></g>
  <g transform="translate(750,597)"><use href="#dial"/><polygon points="51,58 40,4 61,56" fill="#000" stroke="#fff" stroke-width="1.5"/></g>
</svg>
<div class="gauge-label abs" style="left:515px;top:565px">Member Name Verification</div>
<div class="gauge-label abs" style="left:730px;top:565px">Rental Address Verification</div>
<div class="gauge-label abs" style="left:515px;top:663px">Member Contact Verification</div>
<div class="gauge-label abs" style="left:734px;top:663px">Landlord Contact Information</div>
<div class="abs" style="left:537px;top:683px;display:flex;gap:12px;color:#fff">
  <span class="legend"><i class="sw" style="background:var(--soft)"></i>Needs Attention</span>
  <span class="legend"><i class="sw" style="background:var(--bright)"></i>Can Wait</span>
  <span class="legend" style="margin-left:10px"><i class="sw" style="background:var(--deep)"></i>Verified</span>
</div>

<section class="panel abs" style="left:16px;top:717px;width:486px;height:211px">
  <h2 class="panel-title abs" style="left:19px;top:10px">5 Factors That Determine Your Credit Score</h2>
  <svg class="abs" style="left:14px;top:35px" width="180" height="170" viewBox="0 0 180 170" role="img" aria-label="Pie chart of credit score factors">
    <g stroke="#fff" stroke-width="4" stroke-linejoin="round">
      <path d="M78 76.6 L6.1 79.1 A72 72 0 0 1 114 14.2 Z" fill="var(--pie-grey)"/>
      <path d="M91.7 72.4 L133 13.4 A72 72 0 0 1 162.6 59.9 Z" fill="var(--pie-teal)"/>
      <path d="M89.1 84.2 L160.8 77.9 A72 72 0 0 1 130.4 143.2 Z" fill="var(--pie-dark)"/>
      <path d="M77.3 85.3 L111.1 148.9 A72 72 0 0 1 6 95.3 Z" fill="var(--pie-blue)"/>
    </g>
  </svg>
  <div class="abs" style="left:194px;top:64px;display:flex;flex-direction:column;gap:13px">
    <span class="factor"><i class="sw" style="background:var(--pie-teal)"></i>Payment History</span>
    <span class="factor"><i class="sw" style="background:var(--pie-grey)"></i>Amount Owed</span>
    <span class="factor"><i class="sw" style="background:var(--pie-dark)"></i>Types of Credit</span>
    <span class="factor"><i class="sw" style="background:var(--pie-blue)"></i>New Credit</span>
  </div>
</section>

<section class="panel abs" style="left:511px;top:717px;width:377px;height:211px">
  <div class="abs" style="left:16px;top:20px;display:flex;flex-direction:column;gap:8px">
    <span class="legend"><i class="sw" style="background:var(--pie-teal)"></i>&nbsp;Payment History 30%</span>
    <span class="legend"><i class="sw" style="background:var(--pie-grey)"></i>&nbsp;Amount Owed 30%</span>
    <span class="legend"><i class="sw" style="background:var(--pie-dark)"></i>&nbsp;Types of Credit 15%</span>
    <span class="legend"><i class="sw" style="background:var(--pie-blue)"></i>&nbsp;New Credit 10%</span>
  </div>
</section>
<a class="cta abs">Continue to Your Rent Profile
  <svg class="abs" style="left:282px;top:22px" width="32" height="34" viewBox="0 0 32 34"><polygon points="0,0 30,17 0,34" fill="#fff"/></svg>
</a>

<footer class="footer abs">
  <div class="tip" style="left:16px"><h3>History</h3><p>Have you ever made late payments?</p></div>
  <div class="tip" style="left:164px"><h3>Balance</h3><p>Do you have high balances?</p></div>
  <div class="tip" style="left:298px"><h3>Account Age</h3><p>How old are your accounts?</p></div>
  <div class="tip" style="left:444px"><h3>New Credit</h3><p>Have you opened a new account lately?</p></div>
  <div class="tip" style="left:586px"><h3>Types</h3><p>What type of account do you have?</p></div>
  <span class="more" style="left:101px">More Info</span>
  <span class="more" style="left:243px">More Info</span>
  <span class="more" style="left:384px">More Info</span>
  <span class="more" style="left:524px">More Info</span>
  <span class="more" style="left:665px">More Info</span>
</footer>
</body>
</html>
```